Harbor Ridge Advisory Group (HRA) Business Card

Front Side, add Company Logo
1.) Harbor Ridge Advisory Group
Director of Operations
Okafor, Dwayne M
(555) 217 4836
718 n Maple Ave Suite 200 PMB2281
Brookhaven, CA 90415
Dwayne@HarborRidgeAdv.example
www.harborridgeadv.example
2.) Veteran-Owned Business (with Small Falcon Crest)

Back Side
- Pictures are ideas of what you can add. The description is what HRA does.
1.) Business Partners:
- Lumora Business
- Q&V Business
- Teltrix Business
2.) What we do
- Broker of Internet service (partners above)
- Project Management/ Contract Management
- Government Contracts

```html
<!DOCTYPE html>
<html lang="en">
<head>
<meta charset="utf-8">
<title>Harbor Ridge Advisory Group – Business Card</title>
<link href="https://fonts.googleapis.com/css2?family=Questrial&display=swap" rel="stylesheet">
<style>
  :root {
    --backdrop: #e3e4e6;
    --card: #141414;
    --gold: #f2b705;
    --ink: #e9e9e9;
    --rule: #6b6b6b;
    --tile: #f4f4f4;
    --tile-ink: #1b1b1b;
  }
  * { box-sizing: border-box; margin: 0; padding: 0; }
  html, body { width: 1200px; height: 800px; overflow: hidden; }
  body {
    background: var(--backdrop);
    font-family: "Questrial", "Century Gothic", sans-serif;
    position: relative;
  }
  .card {
    position: absolute;
    top: 246px;
    width: 540px;
    height: 309px;
    background: var(--card);
    border-radius: 4px;
    box-shadow: 0 10px 28px rgba(0,0,0,.22);
    color: var(--ink);
  }
  .card--back { left: 40px; }
  .card--front { left: 620px; }

  /* Brand mark */
  .brand-mark {
    position: absolute;
    width: 124px; height: 124px;
    border: 2px solid var(--gold);
    border-radius: 50%;
    display: flex; align-items: center; justify-content: center;
    text-align: center;
    color: var(--gold);
    font-size: 13px;
    line-height: 1.3;
    letter-spacing: .04em;
    padding: 14px;
  }
  .card--front .brand-mark { left: 52px; top: 132px; }
  .card--back .brand-mark { left: 300px; top: 22px; width: 104px; height: 104px; font-size: 11px; }

  /* Front */
  .holder { position: absolute; left: 40px; top: 30px; }
  .holder__name { color: var(--gold); font-size: 21px; font-weight: 400; }
  .holder__title { font-size: 14px; margin-top: 4px; }
  .divider {
    position: absolute; left: 222px; top: 128px;
    width: 1px; height: 140px; background: var(--rule);
  }
  .contact { position: absolute; left: 242px; top: 140px; list-style: none; font-size: 14px; }
  .contact li { display: flex; align-items: flex-start; gap: 8px; margin-bottom: 7px; line-height: 1.25; }
  .contact svg { flex: none; width: 13px; height: 13px; margin-top: 2px; fill: var(--gold); }

  /* Back */
  .partners { position: absolute; left: 0; right: 0; top: 136px; text-align: center; }
  .section-title { color: var(--gold); font-size: 17px; font-weight: 400; }
  .partner-list { display: flex; justify-content: center; gap: 12px; margin-top: 8px; list-style: none; }
  .partner {
    background: var(--tile); color: var(--tile-ink);
    font-size: 11px; padding: 6px 9px;
    display: flex; align-items: center; gap: 5px;
  }
  .partner__dot { width: 8px; height: 8px; border-radius: 50%; background: var(--tile-ink); }
  .services { position: absolute; left: 0; right: 0; top: 212px; text-align: center; }
  .service-list { list-style: none; font-size: 14px; margin-top: 4px; line-height: 1.35; }
</style>
</head>
<body>

<section class="card card--back" aria-label="Card back">
  <div class="brand-mark">Harbor Ridge Advisory Group</div>
  <div class="partners">
    <h2 class="section-title">Business Partners</h2>
    <ul class="partner-list">
      <li class="partner"><span class="partner__dot"></span>Q&amp;V Business</li>
      <li class="partner"><span class="partner__dot"></span>Lumora Business</li>
      <li class="partner"><span class="partner__dot"></span>Teltrix Business</li>
    </ul>
  </div>
  <div class="services">
    <h2 class="section-title">What we do</h2>
    <ul class="service-list">
      <li>Broker of Internet service (partners above)</li>
      <li>Project Management/ Contract Management</li>
      <li>Government Contracts</li>
    </ul>
  </div>
</section>

<section class="card card--front" aria-label="Card front">
  <div class="holder">
    <h1 class="holder__name">Okafor, Dwayne M</h1>
    <p class="holder__title">Director of Operations</p>
  </div>
  <div class="brand-mark">Harbor Ridge Advisory Group</div>
  <div class="divider"></div>
  <ul class="contact">
    <li>
      <svg viewBox="0 0 24 24" aria-hidden="true"><path d="M6.6 10.8a15 15 0 0 0 6.6 6.6l2.2-2.2a1 1 0 0 1 1-.25 11.4 11.4 0 0 0 3.6.57 1 1 0 0 1 1 1V20a1 1 0 0 1-1 1A17 17 0 0 1 3 4a1 1 0 0 1 1-1h3.5a1 1 0 0 1 1 1c0 1.25.2 2.45.57 3.57a1 1 0 0 1-.25 1z"/></svg>
      <span>(555) 217 4836</span>
    </li>
    <li>
      <svg viewBox="0 0 24 24" aria-hidden="true"><path d="M2 5h20v14H2zm2 2v.5l8 5 8-5V7l-8 5z"/></svg>
      <span>Dwayne@HarborRidgeAdv.example</span>
    </li>
    <li>
      <svg viewBox="0 0 24 24" aria-hidden="true"><path d="M12 2a10 10 0 1 0 0 20 10 10 0 0 0 0-20zm0 2.2c1 1.2 1.8 3 2.1 5.3H9.9C10.2 7.2 11 5.4 12 4.2zM4.3 11.5h3.5c0 1.7.3 3.3.8 4.6A8 8 0 0 1 4.3 11.5zm5.6 0h4.2c0 2-.5 3.9-2.1 5.9-1.6-2-2.1-3.9-2.1-5.9zm6.3 0h3.5a8 8 0 0 1-4.3 4.6c.5-1.3.8-2.9.8-4.6z"/></svg>
      <span>www.harborridgeadv.example</span>
    </li>
    <li>
      <svg viewBox="0 0 24 24" aria-hidden="true"><path d="M12 2a7 7 0 0 0-7 7c0 5 7 13 7 13s7-8 7-13a7 7 0 0 0-7-7zm0 9.5A2.5 2.5 0 1 1 12 6.5a2.5 2.5 0 0 1 0 5z"/></svg>
      <span>718 n Maple Ave Suite 200 PMB2281<br>Brookhaven, CA 90415</span>
    </li>
  </ul>
</section>

</body>
</html>
```